Scuba diving website (Only 1 page. If nice all website later for you)

The payment is for one page only. We are looking for the main design of our new website. For test you will have to redesign the page that is attached to this description. If we like the style we will choose you as the main designer for the whole website (around 20 pages).
The website is about scuba diving. It targets world wide in 4 languages dive centers, divers, underwater photographers, dive sites research, fish species info many more to come. The website is bulid on strong fondation and expect high visits. Developpment is done.
We need now to find the perfect design. The page to redesign is a page about a "dive center" that subscribe to the website where he presents himself and fills it's information. (like a plimbook page).
We are looking for between MODERN and MINIMAL design, but most of all a CLEAN design. See below some design website we like
http://velorint.com/pathe/
http://www.quandrell.com/
http://www.paltravex.com/
http://widgets.tarnimello.com/
For the color stay around the blue and orange. The page width should be 1024px.
Updates
You can use small diving pictures for presenting the "Neighbouring dive sites" in the page. (instead of the red and white flag)
Target Market(s)
We target people willing to go on holiday for diving. We target photographer, cameraman who wants to share picture of their dive, we target people who have an interest for fish species (they can tag more than 32000 different species on their picture/video). We target dive centers who want to advertise on the website by creating their own page

```html
<!DOCTYPE html>
<html lang="en">
<head>
<meta charset="utf-8">
<title>Deepwater Divers – Dive Center</title>
<link href="https://fonts.googleapis.com/css2?family=Alegreya:wght@400;500&family=Open+Sans:wght@400;600&display=swap" rel="stylesheet">
<style>
:root{
  --blue:#2f9be0;
  --orange:#f39a2b;
  --ink:#333;
  --muted:#666;
  --panel:#f4f4f4;
  --rule:#e6e6e6;
  --footer:#464646;
  --footer-text:#ddd;
}
*{box-sizing:border-box;margin:0;padding:0}
html,body{width:1200px;height:2229px;overflow:hidden}
body{position:relative;background:#fff;font-family:"Alegreya",Georgia,serif;color:var(--ink)}
.abs{position:absolute}

/* header */
.brand-dot{left:186px;top:38px;width:40px;height:40px;border-radius:50%;background:var(--blue)}
.brand{left:243px;top:29px;color:var(--orange);font-family:"Open Sans",Arial,sans-serif;font-size:26px;line-height:34px;text-transform:uppercase}
.account{left:860px;top:27px;display:flex;align-items:center;font-size:15px}
.account a{color:var(--ink);text-decoration:underline;margin-right:14px}
.flags{display:flex;gap:4px;margin-left:4px}
.flags span{width:22px;height:12px;display:block}
.nav{left:461px;top:75px;width:572px;display:flex;justify-content:space-between;font-size:15px}
.nav a{color:var(--ink);text-decoration:none;padding-bottom:5px}
.nav a.active{border-bottom:3px solid var(--blue)}

/* hero */
.hero{left:0;top:130px;width:1200px;height:152px;border-bottom:4px solid var(--orange);display:flex}
.hero-shot{height:148px;border-right:3px solid rgba(255,255,255,.6)}
.hero-shot:last-child{border-right:0}
.hero-place{left:191px;top:238px;width:148px;height:44px;background:rgba(0,0,0,.35);color:#fff;font-size:28px;line-height:44px;padding-left:18px}

/* info panel */
.panel{left:0;top:286px;width:1200px;height:578px;background:var(--panel)}
.section-title{color:var(--blue);font-family:"Open Sans",Arial,sans-serif;font-weight:400;font-size:27px;line-height:34px;text-transform:uppercase;border-bottom:3px solid #ece5dc;padding-bottom:3px}
.team-card{width:172px;height:114px;border:2px solid #9a9a9a;color:#fff;text-align:center;padding-top:46px;line-height:17px;text-shadow:0 1px 2px rgba(0,0,0,.6)}
.team-card b{display:block;font-weight:400;font-size:19px}
.team-card i{font-style:normal;font-size:15px}
.facilities{list-style:none}
.fac-item{font-size:15px;height:31px;display:flex;align-items:center;gap:11px}
.rating-row{left:684px;width:280px;height:20px;font-family:"Open Sans",Arial,sans-serif;font-size:11.5px;line-height:20px;color:#444}
.stars{position:absolute;left:171px;top:1px}
.btn{display:block;text-align:center;color:#fff;text-decoration:none}
.btn-review{left:682px;top:775px;width:140px;height:25px;background:var(--orange);font-family:"Open Sans",Arial,sans-serif;font-size:11.5px;line-height:25px}

/* gallery */
.pager{top:899px;height:22px;background:var(--blue);color:#fff;font-size:13px;line-height:22px;text-align:center}
.thumbs{left:212px;top:933px;display:grid;grid-template-columns:repeat(3,56px);column-gap:11px;row-gap:9px}
.thumb{width:56px;height:42px}
.photo-nav{left:814px;top:896px;width:184px;font-size:15px;color:var(--blue);display:flex;justify-content:space-between}
.photo{left:455px;top:927px;width:552px;height:286px;
  background:
    radial-gradient(ellipse 30% 22% at 16% 16%,#8b8f8c,transparent 70%),
    radial-gradient(ellipse 22% 20% at 86% 18%,#7c807c,transparent 70%),
    radial-gradient(ellipse 36% 26% at 42% 40%,#6d6f69,transparent 70%),
    radial-gradient(ellipse 26% 16% at 78% 44%,#5f625d,transparent 70%),
    radial-gradient(ellipse 50% 40% at 48% 78%,#52d0c4,transparent 75%),
    linear-gradient(180deg,#23474a 0%,#2f8f93 30%,#36b5ad 55%,#2aa09d 80%,#1f7f84 100%)}
.rule{left:199px;top:1297px;width:855px;height:1px;background:var(--rule)}

/* map */
.map-title{left:208px;top:1344px;font-weight:400;font-size:27px;line-height:32px}
.map{left:200px;top:1380px;width:790px;height:222px;
  background:
    radial-gradient(ellipse 30% 22% at 42% 12%,#5a6a45,transparent 75%),
    radial-gradient(ellipse 16% 34% at 48% 55%,#4f5f3c,transparent 75%),
    radial-gradient(ellipse 14% 20% at 72% 52%,#6b7650,transparent 75%),
    radial-gradient(ellipse 10% 30% at 98% 70%,#56684a,transparent 75%),
    linear-gradient(100deg,#1e3b7c 0%,#28488c 40%,#2a4d92 70%,#243f80 100%)}
.map-zoom{left:209px;top:1390px;width:14px;height:34px;background:#fff;border:1px solid #bbb;font-family:"Open Sans",Arial,sans-serif;font-size:10px;line-height:16px;text-align:center;color:#555}
.map-type{left:918px;top:1385px;width:66px;height:15px;background:#fff;border:1px solid #bbb;font-family:"Open Sans",Arial,sans-serif;font-size:9px;line-height:13px;padding-left:4px;color:#333}

/* contact / employment / message */
.tab{top:1737px;height:43px;background:#111;border-left:9px solid var(--blue);color:#fff;font-size:18px;letter-spacing:.5px;text-transform:uppercase;line-height:43px;padding-left:12px}
.info{font-size:15.5px;color:var(--muted);line-height:20px}
.btn-blue{background:var(--blue);border-radius:3px;font-size:15px}
.field{left:777px;width:220px;border:1px solid #cfcfcf;font-size:15px;color:var(--muted);padding:0 10px}

/* footer */
.footer{left:0;top:2042px;width:1200px;height:187px;background:var(--footer)}
.foot-title{top:2056px;font-weight:400;font-size:25px;line-height:32px;color:#fff;border-bottom:1px solid #5c5c5c;padding-bottom:2px}
.social{width:29px;height:29px;background:#222;border:2px solid #ddd;color:#fff;font-family:"Open Sans",Arial,sans-serif;font-size:6.5px;text-align:center;line-height:25px;overflow:hidden;white-space:nowrap}
.contrib{width:52px;height:34px;border:2px solid #ddd}
.latest-text{left:474px;top:2103px;width:250px;font-family:"Open Sans",Arial,sans-serif;font-size:11.5px;line-height:15px;color:var(--footer-text)}
.copyright{left:474px;top:2198px;font-family:"Open Sans",Arial,sans-serif;font-size:11px;color:var(--footer-text)}
.copyright span{color:var(--orange)}
</style>
</head>
<body>

<!-- header -->
<div class="abs brand-dot"></div>
<div class="abs brand">Deepwater<br>Divers</div>
<div class="abs account">
  <a href="#">Sign in</a><a href="#">Join</a>
  <div class="flags">
    <span style="background:linear-gradient(#1f3b8a 0 40%,#fff 40% 60%,#c8102e 60%)"></span>
    <span style="background:linear-gradient(90deg,#1f3b8a 0 33%,#fff 33% 66%,#d52b1e 66%)"></span>
    <span style="background:linear-gradient(#c60b1e 0 25%,#ffc400 25% 75%,#c60b1e 75%)"></span>
  </div>
</div>
<nav class="abs nav">
  <a class="active" href="#">Home</a><a href="#">Latest</a><a href="#">Photos</a><a href="#">Videos</a><a href="#">Fauna</a><a href="#">Dive site</a><a href="#">Dive center</a><a href="#">Divers</a><a href="#">Forum</a>
</nav>

<!-- hero -->
<div class="abs hero">
  <div class="hero-shot" style="width:177px;background:radial-gradient(ellipse 60% 50% at 40% 60%,#2c7f86,transparent 75%),linear-gradient(160deg,#0f4e57,#1b6a70 50%,#0c3b44)" role="img" aria-label="Coral reef seen from above"></div>
  <div class="hero-shot" style="width:175px;background:radial-gradient(ellipse 50% 45% at 50% 40%,#3a8f94,transparent 75%),linear-gradient(180deg,#16606a,#0f4951)" role="img" aria-label="Reef wall in clear water"></div>
  <div class="hero-shot" style="width:201px;background:radial-gradient(ellipse 55% 40% at 45% 75%,#2e5f6a,transparent 75%),linear-gradient(170deg,#2a8e99,#1d6f7a 55%,#174f58)" role="img" aria-label="Diver fins in open water"></div>
  <div class="hero-shot" style="width:251px;background:radial-gradient(ellipse 35% 45% at 55% 35%,#5aa3b4,transparent 75%),radial-gradient(ellipse 40% 40% at 45% 85%,#1b3f4a,transparent 75%),linear-gradient(180deg,#2c8fa0,#1b6a78)" role="img" aria-label="Smiling diver in a mask underwater"></div>
  <div class="hero-shot" style="width:229px;background:radial-gradient(ellipse 50% 50% at 40% 50%,#3a8c8a,transparent 75%),linear-gradient(180deg,#1d7076,#13545a)" role="img" aria-label="Sea fans on the reef"></div>
  <div class="hero-shot" style="width:167px;background:radial-gradient(ellipse 60% 50% at 60% 40%,#2d7f7a,transparent 75%),linear-gradient(180deg,#135a60,#0d424a)" role="img" aria-label="Soft corals in blue water"></div>
</div>
<div class="abs hero-place">Indonesia</div>

<!-- info panel -->
<div class="abs panel"></div>
<h2 class="abs section-title" style="left:200px;top:322px;width:404px">The Team</h2>

<div class="abs team-card" style="left:202px;top:383px;background:radial-gradient(ellipse 40% 50% at 50% 45%,#9a8a74,transparent 75%),linear-gradient(150deg,#6b6a5e,#3f3e38)" role="img" aria-label="Portrait of dive master Mira"><b>Mira</b><i>Dive master</i></div>
<div class="abs team-card" style="left:429px;top:383px;background:radial-gradient(ellipse 40% 50% at 45% 40%,#8a7560,transparent 75%),linear-gradient(150deg,#2e2e2e,#6e6252)" role="img" aria-label="Portrait of instructor Teo in a mask"><b>Teo</b><i>Instructor</i></div>
<div class="abs team-card" style="left:202px;top:539px;background:radial-gradient(ellipse 40% 50% at 50% 45%,#a0876c,transparent 75%),linear-gradient(150deg,#5a5550,#4a4a48)" role="img" aria-label="Portrait of dive master Arlo"><b>Arlo</b><i>Dive master</i></div>
<div class="abs team-card" style="left:429px;top:539px;background:radial-gradient(ellipse 30% 40% at 50% 30%,#a39a90,transparent 75%),linear-gradient(180deg,#9a9ea2,#5c6064)" role="img" aria-label="Photo of instructor Sela waving from the sea"><b>Sela</b><i>Instructor</i></div>
<div class="abs team-card" style="left:202px;top:682px;background:radial-gradient(ellipse 35% 45% at 50% 40%,#8c7a66,transparent 75%),linear-gradient(180deg,#6a8a98,#2f4a4f)" role="img" aria-label="Portrait of dive master Ines by the sea"><b>Ines</b><i>Dive master</i></div>
<div class="abs team-card" style="left:429px;top:682px;background:radial-gradient(ellipse 35% 45% at 50% 40%,#2aa3b2,transparent 75%),linear-gradient(150deg,#1a7a8a,#0d4f5c)" role="img" aria-label="Underwater photo of instructor Bram"><b>Bram</b><i>Instructor</i></div>

<h2 class="abs section-title" style="left:682px;top:322px;width:326px">Facilities</h2>

<svg width="0" height="0" style="position:absolute">
  <defs>
    <symbol id="tick" viewBox="0 0 14 12"><polyline points="1,6 5,10 13,1" fill="none" stroke="#2f9be0" stroke-width="2.6"/></symbol>
    <symbol id="star" viewBox="0 0 20 20"><polygon points="10,1 12.6,7 19,7.5 14,11.8 15.6,18.5 10,15 4.4,18.5 6,11.8 1,7.5 7.4,7"/></symbol>
  </defs>
</svg>

<ul class="abs facilities" style="left:688px;top:371px">
  <li class="fac-item"><svg width="14" height="12"><use href="#tick"/></svg>Accomodation</li>
  <li class="fac-item"><svg width="14" height="12"><use href="#tick"/></svg>Photos of you dive</li>
  <li class="fac-item"><svg width="14" height="12"><use href="#tick"/></svg>Own Boat</li>
  <li class="fac-item"><svg width="14" height="12"><use href="#tick"/></svg>Rental gear</li>
  <li class="fac-item"><svg width="14" height="12"><use href="#tick"/></svg>Nitrox</li>
  <li class="fac-item"><svg width="14" height="12"><use href="#tick"/></svg>Swimming</li>
  <li class="fac-item"><svg width="14" height="12"><use href="#tick"/></svg>Technical dive</li>
</ul>
<ul class="abs facilities" style="left:845px;top:371px">
  <li class="fac-item"><svg width="14" height="12"><use href="#tick"/></svg>Trimix</li>
  <li class="fac-item"><svg width="14" height="12"><use href="#tick"/></svg>Compressor</li>
  <li class="fac-item"><svg width="14" height="12"><use href="#tick"/></svg>Shop</li>
  <li class="fac-item"><svg width="14" height="12"><use href="#tick"/></svg>Rebreather</li>
  <li class="fac-item"><svg width="14" height="12"><use href="#tick"/></svg>Oxygen on board</li>
  <li class="fac-item"><svg width="14" height="12"><use href="#tick"/></svg>Accomodotion on site</li>
  <li class="fac-item"><svg width="14" height="12"><use href="#tick"/></svg>Accomodotion off site</li>
</ul>

<h2 class="abs section-title" style="left:682px;top:611px;width:290px">Rating</h2>

<div class="abs rating-row" style="top:662px">Professionalism
  <svg class="stars" width="100" height="18" fill="#ddd"><use href="#star" x="0" width="18" height="18" fill="#f5b21c"/><use href="#star" x="20" width="18" height="18"/><use href="#star" x="40" width="18" height="18"/><use href="#star" x="60" width="18" height="18"/><use href="#star" x="80" width="18" height="18"/></svg></div>
<div class="abs rating-row" style="top:683px">Safety
  <svg class="stars" width="100" height="18" fill="#ddd"><use href="#star" x="0" width="18" height="18" fill="#e9522a"/><use href="#star" x="20" width="18" height="18" fill="#e9522a"/><use href="#star" x="40" width="18" height="18"/><use href="#star" x="60" width="18" height="18"/><use href="#star" x="80" width="18" height="18"/></svg></div>
<div class="abs rating-row" style="top:703px">Equipment, Air Quality
  <svg class="stars" width="100" height="18" fill="#ddd"><use href="#star" x="0" width="18" height="18" fill="#e9522a"/><use href="#star" x="20" width="18" height="18" fill="#e9522a"/><use href="#star" x="40" width="18" height="18" fill="#f08a24"/><use href="#star" x="60" width="18" height="18" fill="#f5b21c"/><use href="#star" x="80" width="18" height="18"/></svg></div>
<div class="abs rating-row" style="top:724px">Friendlyness
  <svg class="stars" width="100" height="18" fill="#ddd"><use href="#star" x="0" width="18" height="18" fill="#f5b21c"/><use href="#star" x="20" width="18" height="18" fill="#f5b21c"/><use href="#star" x="40" width="18" height="18" fill="#f5b21c"/><use href="#star" x="60" width="18" height="18"/><use href="#star" x="80" width="18" height="18"/></svg></div>
<div class="abs rating-row" style="top:744px">Price of the service
  <svg class="stars" width="100" height="18" fill="#ddd"><use href="#star" x="0" width="18" height="18" fill="#f5b21c"/><use href="#star" x="20" width="18" height="18" fill="#f5b21c"/><use href="#star" x="40" width="18" height="18" fill="#f5b21c"/><use href="#star" x="60" width="18" height="18"/><use href="#star" x="80" width="18" height="18"/></svg></div>
<a class="abs btn btn-review" href="#">WRITE A REVIEW</a>

<!-- gallery -->
<div class="abs pager" style="left:216px;width:24px">1</div>
<div class="abs pager" style="left:271px;width:42px">Next</div>
<div class="abs thumbs" role="img" aria-label="Grid of fifteen underwater photo thumbnails">
  <div class="thumb" style="background:radial-gradient(circle at 40% 50%,#7a4a5a,#2c3a4e)"></div>
  <div class="thumb" style="background:radial-gradient(circle at 50% 50%,#5f7a4a,#22382a)"></div>
  <div class="thumb" style="background:radial-gradient(circle at 50% 50%,#4e6a3a,#1c2f1a)"></div>
  <div class="thumb" style="background:radial-gradient(circle at 50% 50%,#4fb0e8,#1866b0)"></div>
  <div class="thumb" style="background:radial-gradient(circle at 50% 50%,#5a9ec0,#1d5a84)"></div>
  <div class="thumb" style="background:radial-gradient(circle at 50% 50%,#4a8a6a,#1f3f30)"></div>
  <div class="thumb" style="background:radial-gradient(circle at 50% 50%,#3d8ad8,#154c98)"></div>
  <div class="thumb" style="background:radial-gradient(circle at 50% 50%,#4fa0e8,#1a5cb0)"></div>
  <div class="thumb" style="background:radial-gradient(circle at 50% 50%,#3a7ac0,#153c74)"></div>
  <div class="thumb" style="background:radial-gradient(circle at 40% 60%,#b0583a,#223e6e)"></div>
  <div class="thumb" style="background:radial-gradient(circle at 50% 50%,#7a5a6a,#263e5c)"></div>
  <div class="thumb" style="background:radial-gradient(circle at 50% 50%,#a04a3a,#1f3450)"></div>
  <div class="thumb" style="background:radial-gradient(circle at 50% 50%,#6a5a3a,#2a2c1e)"></div>
  <div class="thumb" style="background:radial-gradient(circle at 50% 50%,#3a4a32,#141f16)"></div>
  <div class="thumb" style="background:radial-gradient(circle at 50% 50%,#2c3a26,#0f1a12)"></div>
</div>
<div class="abs photo-nav"><span>Previous photo</span><span>Next photo</span></div>
<div class="abs photo" role="img" aria-label="Snorkeler swimming in turquoise water between large granite boulders"></div>
<div class="abs rule"></div>

<!-- map -->
<h2 class="abs map-title">Map</h2>
<div class="abs map" role="img" aria-label="Satellite map of the dive center area and nearby islands with dive site markers"></div>
<div class="abs map-zoom">+<br>−</div>
<div class="abs map-type">Satellite ▾</div>

<!-- contact / employment / message -->
<div class="abs tab" style="left:204px;width:218px">Contact</div>
<svg class="abs" style="left:205px;top:1792px" width="18" height="26" viewBox="0 0 18 26"><path d="M9 0C4 0 0 4 0 9c0 7 9 17 9 17s9-10 9-17C18 4 14 0 9 0z" fill="#2f9be0"/><circle cx="9" cy="9" r="3.5" fill="#fff"/></svg>
<div class="abs info" style="left:230px;top:1793px">Coral Drift<br>Harbour lane 14<br>4520 kelara.indonesia</div>
<svg class="abs" style="left:207px;top:1868px" width="22" height="24" viewBox="0 0 22 24"><path d="M5 1l4 5-2.5 3c1.5 3.5 4 6 7 7.5l3-2.5 4.5 4-3 4.5C10 21 2 12 1 4z" fill="#2f9be0"/></svg>
<div class="abs info" style="left:232px;top:1872px">555012-340-118-40021</div>

<div class="abs tab" style="left:494px;width:216px">Employment</div>
<svg class="abs" style="left:494px;top:1793px" width="34" height="26" viewBox="0 0 34 26"><circle cx="7" cy="5" r="4" fill="#2f9be0"/><circle cx="27" cy="5" r="4" fill="#2f9be0"/><circle cx="17" cy="6" r="5" fill="#2f9be0"/><rect x="2" y="10" width="10" height="12" rx="3" fill="#2f9be0"/><rect x="22" y="10" width="10" height="12" rx="3" fill="#2f9be0"/><rect x="11" y="12" width="12" height="14" rx="3" fill="#2f9be0"/></svg>
<div class="abs info" style="left:537px;top:1793px">Coral Drift is currently<br>hiring.</div>
<a class="abs btn btn-blue" href="#" style="left:492px;top:1860px;width:101px;height:32px;line-height:32px">Job offer</a>

<div class="abs tab" style="left:778px;width:216px">Send a message</div>
<div class="abs field" style="top:1793px;height:29px;line-height:27px">Email</div>
<div class="abs field" style="top:1843px;height:90px;padding-top:6px">Message</div>
<a class="abs btn btn-blue" href="#" style="left:925px;top:1956px;width:72px;height:26px;line-height:26px">Send</a>

<!-- footer -->
<footer class="abs footer"></footer>
<h3 class="abs foot-title" style="left:200px;width:228px">Find us on</h3>
<div class="abs social" style="left:199px;top:2100px">Chirp</div>
<div class="abs social" style="left:238px;top:2100px">Feed</div>
<div class="abs social" style="left:279px;top:2100px">Tumbo</div>
<div class="abs social" style="left:199px;top:2142px">plimbook</div>
<div class="abs social" style="left:238px;top:2142px">Circl</div>

<h3 class="abs foot-title" style="left:474px;width:250px">Latest upload</h3>
<p class="abs latest-text">Duis autem vel eum iriure dolor in hendrerit in vulputate velit esse molestie consequat.</p>

<h3 class="abs foot-title" style="left:812px;width:190px">Best contributors</h3>
<div class="abs contrib" style="left:812px;top:2099px;background:radial-gradient(circle at 50% 45%,#c09a7a,#4a7a98)" role="img" aria-label="Contributor photo"></div>
<div class="abs contrib" style="left:875px;top:2099px;background:radial-gradient(circle at 50% 50%,#3ab0bc,#15707c)" role="img" aria-label="Contributor photo"></div>
<div class="abs contrib" style="left:938px;top:2099px;background:radial-gradient(circle at 50% 50%,#8a8478,#4a4a42)" role="img" aria-label="Contributor photo"></div>
<div class="abs contrib" style="left:812px;top:2144px;background:radial-gradient(circle at 50% 50%,#c08a6a,#5a4a40)" role="img" aria-label="Contributor photo"></div>
<div class="abs contrib" style="left:875px;top:2144px;background:radial-gradient(circle at 50% 40%,#e8ecef,#9aa2a8)" role="img" aria-label="Contributor photo"></div>

<p class="abs copyright">Copyright © 2014 <span>DEEPWATER DIVERS</span></p>

</body>
</html>
```